Private Learning Centre in Singapore needs a flyer design

We need a flyer design for our upcoming education fair and also able to use it for day to day purpose. The aim is to attract parents, students to enrol for classes by offering them free trial class/assessment. 2 sided flyer with the front page as the logo only and details on the other page. We would like to see a final design in blue, white and it should be curious and attractive enough not to allow customers to throw it away once they received it.

Education

```html
<!DOCTYPE html>
<html lang="en">
<head>
<meta charset="utf-8">
<title>Bright Grove Academy – Free Trial Class Flyer</title>
<link rel="stylesheet" href="https://fonts.googleapis.com/css2?family=Tinos:wght@400;700&display=swap">
<style>
  :root {
    --brand-blue: #3a55a4;
    --card-white: #f3f3f3;
    --faint-grey: #e4e5e8;
    --stage: #e8e4dd;
    --shadow: rgba(60, 45, 30, 0.28);
  }
  * { box-sizing: border-box; margin: 0; padding: 0; }
  html, body { width: 1200px; height: 942px; overflow: hidden; }
  body {
    background: var(--stage);
    font-family: "Tinos", "Times New Roman", serif;
    color: var(--brand-blue);
    position: relative;
  }
  .flyer-side {
    position: absolute;
    top: 90px;
    width: 536px;
    height: 762px;
    background: var(--card-white);
    box-shadow: 4px 5px 10px var(--shadow);
    overflow: hidden;
  }
  .flyer-front { left: 30px; }
  .flyer-back { left: 634px; }

  /* Front */
  .front-illustration {
    position: absolute;
    left: 330px; top: 540px;
    width: 200px; height: 222px;
    border-radius: 45% 45% 0 0;
    background: radial-gradient(ellipse at 50% 40%, var(--faint-grey) 0%, rgba(228,229,232,0.6) 60%, rgba(228,229,232,0) 100%);
  }
  .brand-lockup {
    position: absolute;
    left: 0; right: 0; top: 0; bottom: 0;
    display: flex; flex-direction: column; align-items: center; justify-content: center; gap: 22px;
  }
  .brand-dot {
    width: 120px; height: 120px; border-radius: 50%;
    background: var(--brand-blue);
  }
  .brand-name {
    font-size: 30px; font-weight: 400; white-space: nowrap;
    letter-spacing: 0.08em; text-transform: uppercase;
    color: var(--brand-blue);
  }

  /* Back */
  .back-illustration {
    position: absolute;
    left: 70px; top: 150px;
    width: 430px; height: 440px;
    border-radius: 50% 50% 8% 8%;
    background: radial-gradient(ellipse at 50% 45%, rgba(228,229,232,0.95) 0%, rgba(228,229,232,0.55) 55%, rgba(228,229,232,0) 100%);
  }
  .title-block {
    position: absolute; left: 44px; width: 454px; top: 46px;
  }
  .rule-thin { height: 3px; background: var(--brand-blue); }
  .rule-thick { height: 7px; background: var(--brand-blue); }
  .headline {
    font-size: 64px; font-weight: 400; text-align: center;
    line-height: 88px; white-space: nowrap;
  }
  .intro, .subjects {
    position: absolute; left: 34px; right: 34px;
    font-size: 18px; line-height: 23px; text-align: center;
  }
  .intro { top: 200px; }
  .subjects { top: 340px; }
  .intro strong { font-weight: 700; }

  .social-link {
    position: absolute; left: 58px; top: 612px;
    display: flex; align-items: center; gap: 8px;
    font-size: 16px; line-height: 20px;
  }
  .social-square { width: 20px; height: 20px; background: var(--brand-blue); }

  .contact-block {
    position: absolute; left: 150px; width: 320px; top: 610px;
    text-align: center; font-style: normal;
  }
  .contact-name {
    display: inline-block;
    font-size: 20px; line-height: 26px;
    border-bottom: 1.5px solid var(--brand-blue);
    padding: 0 6px 1px;
  }
  .contact-phone {
    margin-top: 8px;
    font-size: 20px; line-height: 22px;
    display: flex; justify-content: center; align-items: center; gap: 10px;
  }
  .contact-phone svg { width: 20px; height: 16px; }
  .contact-line { font-size: 16px; line-height: 22px; }
  .bottom-band {
    position: absolute; left: 0; right: 0; bottom: 0; height: 10px;
    background: var(--brand-blue);
  }
</style>
</head>
<body>

  <section class="flyer-side flyer-front">
    <div class="front-illustration" role="img" aria-label="Faint silhouette of a child reading a book"></div>
    <div class="brand-lockup">
      <span class="brand-dot"></span>
      <span class="brand-name">Bright Grove Academy</span>
    </div>
  </section>

  <section class="flyer-side flyer-back">
    <div class="back-illustration" role="img" aria-label="Faint tree with a child reading beneath it"></div>

    <header class="title-block">
      <div class="rule-thin"></div>
      <h1 class="headline">Free Trial Class</h1>
      <div class="rule-thick"></div>
    </header>

    <p class="intro"><strong>Bright Grove Academy</strong> is where you can develop academic and life skills. Our teachers are the heartbeat of the business. They inspire and nurture students, helping them surpass their expectations.</p>

    <p class="subjects">We cover English, Mathematics and Science from Primary and Secondary Levels.</p>

    <div class="social-link">
      <span class="social-square"></span>
      <span>Chatterbook</span>
    </div>

    <address class="contact-block">
      <div class="contact-name">Bright Grove Academy</div>
      <div class="contact-phone">
        <svg viewBox="0 0 20 16" aria-hidden="true">
          <path d="M1 5 Q10 -1 19 5 L17 8 L14 6 L14 4 Q10 2.5 6 4 L6 6 L3 8 Z" fill="var(--brand-blue)"/>
          <path d="M5 8 L7 6 L13 6 L15 8 L16 15 L4 15 Z" fill="var(--brand-blue)"/>
          <circle cx="10" cy="10.5" r="2.2" fill="var(--card-white)"/>
        </svg>
        <span>6123 4578</span>
      </div>
      <div class="contact-line">48 Meranti Lane S419022</div>
      <div class="contact-line">hello@brightgroveacademy.com</div>
    </address>

    <div class="bottom-band"></div>
  </section>

</body>
</html>
```